Quoralt Business Card Design

We need a modern great looking premium business card design that can be customized by person that also displays a contact QR code. It should match our existing branding and website Quoralt.com . We need to be able to upload it to pimb for continued customization and use across a good size company.

```html
<!DOCTYPE html>
<html lang="en">
<head>
<meta charset="utf-8">
<title>Quoralt Business Card</title>
<link href="https://fonts.googleapis.com/css2?family=Montserrat:wght@600;700&family=Open+Sans:wght@400;600&display=swap" rel="stylesheet">
<style>
  :root {
    --stage: #2a2a2a;
    --navy: #1b3a7a;
    --navy-deep: #15306a;
    --navy-light: #2a4d94;
    --ink: #4a4a4a;
    --paper: #ffffff;
    --paper-shade: #eeeeee;
    --code-tint: #e3e8f2;
  }
  * { box-sizing: border-box; margin: 0; padding: 0; }
  html, body { width: 1200px; height: 688px; overflow: hidden; }
  body {
    background: var(--stage);
    font-family: "Open Sans", sans-serif;
    position: relative;
  }
  .card {
    position: absolute;
    top: 196px;
    width: 520px;
    height: 297px;
    border-radius: 3px;
    overflow: hidden;
  }
  .card--back { left: 60px; }
  .card--front {
    left: 620px;
    background: linear-gradient(135deg, var(--paper) 55%, var(--paper-shade));
  }
  .back-pattern {
    position: absolute;
    inset: 0;
    background: linear-gradient(135deg, var(--navy-light), var(--navy) 45%, var(--navy-deep));
  }
  .wordmark {
    font-family: "Montserrat", sans-serif;
    font-weight: 700;
    letter-spacing: 0.5px;
    display: flex;
    align-items: center;
    gap: 12px;
    white-space: nowrap;
  }
  .wordmark__square { width: 26px; height: 26px; }
  .card--back .wordmark {
    position: absolute;
    left: 50%;
    top: 50%;
    transform: translate(-50%, -50%);
    color: var(--paper);
    font-size: 38px;
  }
  .card--back .wordmark__square { background: var(--paper); }
  .card--front .wordmark {
    position: absolute;
    left: 40px;
    top: 50%;
    transform: translateY(-50%);
    color: var(--navy);
    font-size: 40px;
  }
  .card--front .wordmark__square { background: var(--navy); width: 30px; height: 30px; }
  .divider {
    position: absolute;
    left: 300px;
    top: 62px;
    width: 1px;
    height: 173px;
    background: var(--navy);
  }
  .contact {
    position: absolute;
    left: 322px;
    top: 66px;
    color: var(--ink);
    font-size: 11.5px;
    line-height: 1.45;
    white-space: nowrap;
  }
  .contact__name {
    font-family: "Montserrat", sans-serif;
    font-weight: 700;
    font-size: 16px;
    color: var(--navy);
    letter-spacing: 0.3px;
  }
  .contact__role { font-size: 12.5px; margin-bottom: 12px; }
  .contact__address { margin-bottom: 12px; }
  .contact__list { list-style: none; }
  .contact__list li { display: flex; align-items: center; gap: 7px; }
  .contact__list svg { width: 10px; height: 10px; fill: var(--navy); flex: none; }
  .contact-code {
    position: absolute;
    right: 22px;
    bottom: 22px;
    width: 54px;
    height: 54px;
    background: var(--code-tint);
    border: 2px solid var(--navy);
    border-radius: 2px;
  }
</style>
</head>
<body>
  <section class="card card--back">
    <div class="back-pattern" role="img" aria-label="Embossed repeating geometric brand pattern in navy tones"></div>
    <div class="wordmark"><span class="wordmark__square"></span>Quoralt</div>
  </section>

  <section class="card card--front">
    <div class="wordmark"><span class="wordmark__square"></span>Quoralt</div>
    <div class="divider"></div>
    <div class="contact">
      <p class="contact__name">DANIEL REYES</p>
      <p class="contact__role">CEO &amp; Founder</p>
      <p class="contact__address">Unit 12, 48 Alder Ln<br>Fenwick City, OK 70000</p>
      <ul class="contact__list">
        <li>
          <svg viewBox="0 0 10 10" aria-hidden="true"><path d="M2 0.5 L3.6 2.6 L2.8 3.6 Q4 6 6.4 7.2 L7.4 6.4 L9.5 8 L8.4 9.5 Q4.5 9.5 2 7 Q0.5 5 0.5 1.6 Z"/></svg>
          (800) 555-0142
        </li>
        <li>
          <svg viewBox="0 0 10 10" aria-hidden="true"><rect x="0.5" y="2" width="9" height="6.5" rx="0.6"/><path d="M0.8 2.3 L5 5.6 L9.2 2.3" stroke="#fff" stroke-width="0.9" fill="none"/></svg>
          sales@quoralt.com
        </li>
        <li>
          <svg viewBox="0 0 10 10" aria-hidden="true"><circle cx="5" cy="5" r="4.5"/><path d="M0.5 5 H9.5 M5 0.5 Q2.6 5 5 9.5 M5 0.5 Q7.4 5 5 9.5" stroke="#fff" stroke-width="0.7" fill="none"/></svg>
          www.quoralt.com
        </li>
      </ul>
    </div>
    <div class="contact-code" role="img" aria-label="Placeholder for the contact QR code"></div>
  </section>
</body>
</html>
```